Classic Personal Business Card in Regatta Dunmore Hale Style (Horizontal - Raised Ink)

If you ever seen a Dunmore Hale Regatta shirt, you will know that the signature of that shirt is small monogrammed icon on the left pocket. I envision my personal business card using some of these elements. I am in the oil exploration industry, which is very conservative and I want a card that looks great but still reflects that classic conservatism. I specifically do land management work, which means I determine who owns mineral rights, I lease those rights for larger companies to then drill for crude oil and natural gas

1. I have designed a small logo (which definitely could use some help) that I would like to be pretty small, centered in the middle of the card, and near the top of the card (color - navy blue or similar) Please feel free to make this logo infinitely better. However, I am not looking for anything abstract/

2. I want my name and designation (Marcus J. Thornbury, RPL) centered in the middle of the card. As far as font, I'm looking for a classic, strong (almost masculine) cursive font (I realize masculine + cursive is a little oxymoronic) and I would like it to the color to be Gold.

3. I would like my name (see above) to sit on top of a thin, centered navy blue (or similar) line as if it were almost a signature on a line. I want the lower-case letters that normally would dip below the line (which is y and p in my case) to do the same. I'll attach an example to help illustrate what I mean.

4. The rest of the card is my contact information. Because I am shoot for a more centered and balance look, I would like the placement of my contact information to also be centered and balance. Font should be a very classic, professional font. My first inclination is to use black for the color but I'm open to other suggestions.

Contact information:

Phone: (XXX) XXX-XXXX
Email: xxxxxxx@mailbox-example.net

Important Note: My hope is to have these printed with Raised Ink on High Quality High Quality Card Stock so it must conform to this Necessity.

Project Deadline Extended Reason: I am having major internet trouble. So I am not able to look at the submissions and provide feedback in a timely fashion. Also, it is difficult to access the site from just my phone. Added Saturday, November 22, 2014

Target Market(s)

US Oil Executives

Industry/Entity Type

Conservative

Contact Information for Business Card

I've posted a new logo that needs some clean up and a new idea for the top and bottom border of the card. I would like the logo to be centered in the top border with a white barrier on either side between the logo and the border. I've also posted color codes below.

Thanks

Requirements
Must have
• Color Codes:
• Blue: R - 0 G - 0 B - 102
• Gold R - 102 G - 102 B - 0

```html
<!DOCTYPE html>
<html lang="en">
<head>
<meta charset="utf-8">
<title>Marcus J. Thornbury, RPL — Business Card</title>
<link rel="stylesheet" href="https://fonts.googleapis.com/css2?family=Pinyon+Script&family=Tinos:wght@400&display=swap">
<style>
  :root {
    --backdrop: #e9e6e1;
    --card: #ffffff;
    --band-blue: #2a87cf;
    --line-blue: #2a87cf;
    --gold: #f2c811;
    --ink: #111111;
  }
  * { box-sizing: border-box; margin: 0; padding: 0; }
  html, body {
    width: 1200px;
    height: 900px;
    overflow: hidden;
    background: var(--backdrop);
  }
  .canvas {
    width: 1200px;
    height: 900px;
    display: flex;
    align-items: center;
    justify-content: center;
  }
  .business-card {
    position: relative;
    width: 1000px;
    height: 572px;
    background: var(--card);
    box-shadow: 0 6px 24px rgba(0,0,0,0.18);
  }
  .side-band {
    position: absolute;
    width: 48px;
    background: var(--band-blue);
  }
  .side-band--left { left: 14px; top: 40px; bottom: 36px; }
  .side-band--right { right: 14px; top: 36px; bottom: 40px; }

  .card-content {
    position: absolute;
    inset: 0;
    display: flex;
    flex-direction: column;
    align-items: center;
  }
  .brand-mark {
    margin-top: 120px;
    display: flex;
    align-items: center;
    gap: 12px;
    font-family: "Tinos", "Times New Roman", serif;
    font-size: 26px;
    color: var(--band-blue);
    letter-spacing: 0.04em;
    white-space: nowrap;
  }
  .brand-dot {
    width: 22px;
    height: 22px;
    border-radius: 50%;
    background: var(--band-blue);
  }
  .signature {
    margin-top: 70px;
    position: relative;
    width: 520px;
    height: 52px;
    text-align: center;
  }
  .signature-name {
    display: block;
    font-family: "Pinyon Script", cursive;
    font-size: 42px;
    line-height: 1;
    white-space: nowrap;
    color: var(--gold);
    position: relative;
    z-index: 1;
  }
  .signature-line {
    position: absolute;
    left: 0;
    right: 0;
    top: 34px;
    height: 2px;
    background: var(--line-blue);
  }
  .contact {
    margin-top: 6px;
    text-align: center;
    font-family: "Tinos", "Times New Roman", serif;
    font-size: 27px;
    line-height: 1.3;
    color: var(--ink);
    white-space: nowrap;
  }
</style>
</head>
<body>
  <main class="canvas">
    <section class="business-card">
      <div class="side-band side-band--left"></div>
      <div class="side-band side-band--right"></div>
      <div class="card-content">
        <div class="brand-mark">
          <span class="brand-dot"></span>
          <span class="brand-name">Thornbury Land</span>
        </div>
        <div class="signature">
          <span class="signature-name">Marcus J. Thornbury, RPL</span>
          <span class="signature-line"></span>
        </div>
        <div class="contact">
          <p class="contact-phone">+1 555 014 7290</p>
          <p class="contact-email">marcus@mailbox-example.net</p>
        </div>
      </div>
    </section>
  </main>
</body>
</html>
```